HTML Digital Sign layout and code (one page)...save us from the 60's!

Digital Sign for Headquarters Entrance

HTML Digital Sign layout (one page)...save us from the 60's!

Good Day Designers!

We have decided to install Digital Signage in our headquarters building that will replace the “felt boards” that the administrative staff use at our building entrances.

Instead of the information being displayed on the archaic sign boards, it will be presented on a landscaped 50inch LCD screen running at 1920x1080

We are looking for a one page HTML design that encompass the following elements:

+ Our Logo
+ Our Company Name (Vorlan Aerotek)
+ Our "Tag Line" - "Progress Shaped By Practice, Quality Shaped By Dedication"
+ Date and Time
+ A space for Today’s Birthdays (which could be up to 4 people)
+ A space for Today’s Anniversaries (which could be up to 4 people)
+ A space for Today’s Visitor (which could be up to 2 people)
+ A space for a Picture of the Day
+ A space for Weather Forecast (perhaps a graphic)
+ A small "banner" section or strip for scrolling Notices / Alerts (perhaps at the bottom of the page?)

The deliverables for the layout need to include the HTML, applicable CSS, HTML code, etc. We need this to be relatively turnkey.

I have included in the contest package a hi-res JPG and AI for our Company Logo.

From a color pallet perspective:

Light Blue:
RGB - 21, 191,242
HEX - #15BFF2

Dark Blue:
RGB - 0, 70, 154
HEX - #00469A

Additionally, I have done a contest like this before (for another company I was at) and have included a screen shot of that final display.

PLEASE NOTE: IT DOES NOT HAVE TO LOOK EXACTLY LIKE THE ATTACHED SCREEN SHOT FROM THE PREVIOUS CONTEST. Including the screenshot was just to give you a general idea of some inspiration and objectives.

Feedback and questions are encouraged.

Target Market(s)

Our Employees

Industry/Entity Type

Digital

Number of Pages Required

1 page

Requirements
Must have
• + Our Logo
• + Our Company Name (Vorlan Aerotek)
• + Our "Tag Line" - "Progress Shaped By Practice, Quality Shaped By Dedication"
• + Date and Time
• + A space for Today’s Birthdays (which could be up to 4 people)
• + A space for Today’s Anniversaries (which could be up to 4 people)
• + A space for Today’s Visitor (which could be up to 2 people)
• + A space for a Picture of the Day
• + A space for Weather Forecast (perhaps a graphic)
• + A small "banner" section or strip for scrolling Notices / Alerts (perhaps at the bottom of the page?)

```html
<!DOCTYPE html>
<html lang="en">
<head>
<meta charset="utf-8">
<title>Vorlan Aerotek – Entrance Display</title>
<link rel="stylesheet" href="https://fonts.googleapis.com/css2?family=Arimo:ital,wght@0,400;0,700;1,400&display=swap">
<style>
:root{
  --navy:#1d3a8c;
  --link:#0f3f96;
  --ink:#555555;
  --muted:#666666;
  --page:#efefef;
  --card:#ffffff;
  --rule:#dcdcdc;
  --footer:#383838;
  --footer-ink:#d8d8d8;
  --icon:#8a8a8a;
  --notice:#4a4a4a;
}
*{box-sizing:border-box;margin:0;padding:0}
html,body{width:1200px;height:635px;overflow:hidden}
body{
  font-family:"Arimo",Arial,sans-serif;background:var(--page);color:var(--ink);position:relative;
  -webkit-font-smoothing:antialiased;-moz-osx-font-smoothing:grayscale;
}
.display{position:absolute;inset:0;will-change:transform}
h2,h3{font-weight:400}

.masthead{position:absolute;left:0;top:0;width:1200px;height:62px;background:#fff;border-bottom:1px solid #dadada}
.brand{position:absolute;left:70px;top:20px;font-size:17px;font-weight:700;color:var(--navy);letter-spacing:.3px}
.tagline{position:absolute;left:215px;top:26px;font-size:12px;color:#555}
.clock{position:absolute;left:975px;top:17px;display:flex;gap:8px;align-items:flex-start}
.clock-time{font-size:13.5px;color:var(--link);line-height:15px}
.clock-date{font-size:7px;font-style:italic;color:#555;margin-top:3px}

.section-title{position:absolute;font-size:10.5px;color:var(--navy);text-transform:uppercase;letter-spacing:.1px}
.card{position:absolute;background:var(--card);border:1px solid #e2e2e2}

.photo-of-day{position:absolute;left:70px;top:121px;width:359px;height:198px;
  background:linear-gradient(180deg,#a9c3df 0%,#d9e3ee 35%,#f1f3f6 60%,#e4e8ee 100%)}
.feature-heading{position:absolute;left:70px;top:345px;font-size:10.5px;color:var(--link)}
.feature-text{position:absolute;left:70px;width:360px;font-size:7.2px;line-height:15px;color:var(--muted)}

.person{position:absolute;left:15px;width:285px;height:48px}
.avatar{position:absolute;left:0;top:0;width:48px;height:40px;background:linear-gradient(135deg,#d8c2ae,#9d8a7c)}
.person-info{position:absolute;left:66px;top:-1px;font-size:8px;line-height:15px;color:var(--muted);white-space:nowrap}
.person-info b{font-weight:400;color:var(--link)}
.person-info .note{font-size:7.4px;line-height:17px;color:var(--muted)}
.divider{position:absolute;left:15px;width:285px;height:1px;background:var(--rule)}

.weather-text{position:absolute;left:22px;top:18px;width:270px;font-size:7.2px;line-height:15px;color:var(--muted)}
.weather-rule{position:absolute;left:24px;top:88px;width:270px;height:1px;background:var(--rule)}
.forecast{position:absolute;left:28px;top:103px;font-size:7px;color:var(--muted)}
.forecast-now{display:flex;gap:10px;margin-bottom:4px}
.forecast-days{display:flex;gap:20px;margin-left:11px}
.day{text-align:center;width:26px}
.day svg{display:block;margin:2px auto 3px}

.footer{position:absolute;left:0;top:582px;width:1200px;height:53px;background:var(--footer);color:var(--footer-ink)}
.legal{position:absolute;left:68px;top:22px;font-size:7.2px}
.notices{position:absolute;left:300px;top:18px;width:580px;height:17px;overflow:hidden;
  background:var(--notice);border-radius:2px;font-size:7.2px;line-height:17px;white-space:nowrap}
.notices-label{position:absolute;left:0;top:0;z-index:1;height:17px;padding:0 8px;background:var(--link);color:#fff;text-transform:uppercase;letter-spacing:.4px}
.notices-track{position:absolute;left:80px;top:0;display:inline-block;padding-left:100%;animation:ticker 30s linear infinite}
@keyframes ticker{from{transform:translateX(0)}to{transform:translateX(-100%)}}
.follow{position:absolute;left:930px;top:15px;display:flex;align-items:center;gap:7px;font-size:7.2px}
.follow i{display:block;width:20px;height:20px;border-radius:50%;background:var(--icon)}
</style>
</head>
<body>
<div class="display">

<header class="masthead">
  <div class="brand">Vorlan Aerotek</div>
  <div class="tagline">Progress Shaped By Practice, Quality Shaped By Dedication</div>
  <div class="clock">
    <svg width="20" height="26" viewBox="0 0 20 26" aria-hidden="true">
      <circle cx="5" cy="5" r="3" fill="#bbb"/><circle cx="15" cy="5" r="3" fill="#bbb"/>
      <circle cx="10" cy="14" r="8.5" fill="#fff" stroke="#aaa" stroke-width="1.4"/>
      <path d="M10 9v5l3 2" stroke="#999" stroke-width="1.2" fill="none"/>
      <path d="M4 23l2-2M16 23l-2-2" stroke="#aaa" stroke-width="1.4"/>
    </svg>
    <div>
      <div class="clock-time">4:08 pm</div>
      <div class="clock-date">Saturday, 6 September 2014 (GMT+5:30)</div>
    </div>
  </div>
</header>

<h2 class="section-title" style="left:70px;top:95px">Picture of the Day</h2>
<div class="photo-of-day" role="img" aria-label="Picture of the day: a blue and white helicopter parked on snow in front of mountains"></div>
<h3 class="feature-heading">Lorem Ipsum is simply dummy text of the printing and typesetting industry.</h3>
<p class="feature-text" style="top:366px">Lorem Ipsum is simply dummy text of the printing and typesetting industry. Lorem Ipsum has been the industry's standard dummy text ever since the 1500s, when an unknown printer took a galley of type and scrambled it to make a type specimen book. It has survived not only five centuries, but also the leap into electronic typesetting, remaining essentially unchanged. It was popularised in the 1960s with the release of Lettrafold sheets containing Lorem Ipsum passages, and more recently with desktop publishing software like Pagecraft Studio including versions of Lorem Ipsum.</p>
<p class="feature-text" style="top:471px">Lorem Ipsum is simply dummy text of the printing and typesetting industry. Lorem Ipsum has been the industry's standard dummy text ever since the 1500s, when an unknown printer took a galley of type and scrambled it to make a type specimen book. It has survived not only five centuries, but also the leap into electronic typesetting, remaining essentially unchanged.</p>

<h2 class="section-title" style="left:470px;top:95px">Today's Birthdays</h2>
<section class="card" style="left:470px;top:121px;width:314px;height:196px">
  <div class="person" style="top:13px"><div class="avatar" role="img" aria-label="Photo of birthday colleague"></div><div class="person-info">First name : <b>Milo Hartwell</b><br>Last name : <b>Milo Hartwell sm</b><br><span class="note">Lorem Ipsum is simply dummy text of the printing and typesetting...</span></div></div>
  <div class="divider" style="top:67px"></div>
  <div class="person" style="top:77px"><div class="avatar" role="img" aria-label="Photo of birthday colleague"></div><div class="person-info">First name : <b>Milo Hartwell</b><br>Last name : <b>Milo Hartwell sm</b><br><span class="note">Lorem Ipsum is simply dummy text of the printing and typesetting...</span></div></div>
  <div class="divider" style="top:131px"></div>
  <div class="person" style="top:140px"><div class="avatar" role="img" aria-label="Photo of birthday colleague"></div><div class="person-info">First name : <b>Milo Hartwell</b><br>Last name : <b>Milo Hartwell sm</b><br><span class="note">Lorem Ipsum is simply dummy text of the printing and typesetting...</span></div></div>
</section>

<h2 class="section-title" style="left:470px;top:332px">Today's Visitors</h2>
<section class="card" style="left:470px;top:358px;width:314px;height:196px">
  <div class="person" style="top:13px"><div class="avatar" role="img" aria-label="Photo of visitor"></div><div class="person-info">First name : <b>Milo Hartwell</b><br>Last name : <b>Milo Hartwell sm</b><br><span class="note">Lorem Ipsum is simply dummy text of the printing and typesetting...</span></div></div>
  <div class="divider" style="top:67px"></div>
  <div class="person" style="top:77px"><div class="avatar" role="img" aria-label="Photo of visitor"></div><div class="person-info">First name : <b>Milo Hartwell</b><br>Last name : <b>Milo Hartwell sm</b><br><span class="note">Lorem Ipsum is simply dummy text of the printing and typesetting...</span></div></div>
  <div class="divider" style="top:131px"></div>
  <div class="person" style="top:140px"><div class="avatar" role="img" aria-label="Photo of visitor"></div><div class="person-info">First name : <b>Milo Hartwell</b><br>Last name : <b>Milo Hartwell sm</b><br><span class="note">Lorem Ipsum is simply dummy text of the printing and typesetting...</span></div></div>
</section>

<h2 class="section-title" style="left:816px;top:95px">Today's Anniversaries</h2>
<section class="card" style="left:816px;top:121px;width:315px;height:196px">
  <div class="person" style="top:13px"><div class="avatar" role="img" aria-label="Photo of anniversary colleague"></div><div class="person-info">First name : <b>Milo Hartwell</b><br>Last name : <b>Milo Hartwell sm</b><br><span class="note">Lorem Ipsum is simply dummy text of the printing and typesetting...</span></div></div>
  <div class="divider" style="top:67px"></div>
  <div class="person" style="top:77px"><div class="avatar" role="img" aria-label="Photo of anniversary colleague"></div><div class="person-info">First name : <b>Milo Hartwell</b><br>Last name : <b>Milo Hartwell sm</b><br><span class="note">Lorem Ipsum is simply dummy text of the printing and typesetting...</span></div></div>
  <div class="divider" style="top:131px"></div>
  <div class="person" style="top:140px"><div class="avatar" role="img" aria-label="Photo of anniversary colleague"></div><div class="person-info">First name : <b>Milo Hartwell</b><br>Last name : <b>Milo Hartwell sm</b><br><span class="note">Lorem Ipsum is simply dummy text of the printing and typesetting...</span></div></div>
</section>

<h2 class="section-title" style="left:816px;top:332px">Weather&nbsp; Forcast</h2>
<section class="card" style="left:816px;top:358px;width:315px;height:196px">
  <p class="weather-text">Lorem Ipsum has been the industry's standard dummy text ever since the 1500s, when an unknown printer took a galley of type and scrambled it to make a type specimen book. It has survived not only five centuries, but also the leap into electronic typesetting, remaining essentially unchanged...</p>
  <div class="weather-rule"></div>
  <div class="forecast">
    <div class="forecast-now"><span>Delhi&nbsp;&nbsp;&nbsp;32°c</span><span>Mostly Cloudy</span></div>
    <div class="forecast-days">
      <div class="day">Saturday<svg width="14" height="12" viewBox="0 0 14 12" aria-hidden="true"><circle cx="9" cy="4" r="3" fill="#f2b632"/><ellipse cx="6" cy="6" rx="5" ry="3" fill="#7fb3e0"/><path d="M4 9l-1 2M7 9l-1 2" stroke="#3b7bd0"/></svg>32/26</div>
      <div class="day">Sunday<svg width="14" height="12" viewBox="0 0 14 12" aria-hidden="true"><circle cx="9" cy="4" r="3" fill="#f2b632"/><ellipse cx="6" cy="6" rx="5" ry="3" fill="#7fb3e0"/><path d="M4 9l-1 2M7 9l-1 2" stroke="#3b7bd0"/></svg>33/26</div>
      <div class="day">Monday<svg width="14" height="12" viewBox="0 0 14 12" aria-hidden="true"><circle cx="9" cy="4" r="3" fill="#f2b632"/><ellipse cx="6" cy="6" rx="5" ry="3" fill="#7fb3e0"/><path d="M4 9l-1 2M7 9l-1 2" stroke="#3b7bd0"/></svg>33/26</div>
    </div>
  </div>
</section>

<footer class="footer">
  <div class="legal">© 2014 Vorlan Aerotek. All rights reserved &nbsp;/&nbsp; Privacy policy</div>
  <div class="notices" role="marquee" aria-label="Notices and alerts">
    <span class="notices-label">Notices</span>
    <span class="notices-track">Fire drill at 11:00 am on Monday &nbsp;•&nbsp; Hangar 2 closed for maintenance this week &nbsp;•&nbsp; Visitor badges must be worn at all times</span>
  </div>
  <div class="follow"><span>Follow Us :</span><i></i><i></i><i></i><i></i><i></i><i></i></div>
</footer>

</div>
</body>
</html>
```